Popular Golf Club needs attractive brochure

We need a brochure that will attract golfers to come to the Kellaway River area and the Brindlemere Golf Club for their golfing holiday. It also needs to address the availability of a function area and corporate functions in the clubhouse and corporate golf days on the course as well.
It will highlight our direct phone contact numbers and website as well.
We are a 36 Hole Championship Golf Course on the Kellaway River border of NSW and Victoria. 3 hours easy freeway drive from Melbourne. Over 300 sunny days every year. Fabulous golf weather all year round. Raincheck guarantee (if it rains we will give you free golf on you next visit).
The area is a golf and watersport playground. Sandy beaches, the mighty Kellwya River, home of the giant Kellaway Perch, fishing, camping, boating and golf all on your doorstep.
We can arrange Golf packages for individuals and groups including 3 and 4 star accommodation available all year round.

Target Market(s)

Golfers looking for holidays

Industry/Entity Type

Accommodation

Requirements
Must have
• Branding bar and logo. Colours signifying sun, grass and river.
Nice to have
• Smiling happy golfers, particularly more senior age group. Map of location and proximity to Melbourne. Photos of the course. some attached, many more available.

```html
<!DOCTYPE html>
<html lang="en">
<head>
<meta charset="utf-8">
<title>Brindlemere Golf Club Brochure</title>
<link href="https://fonts.googleapis.com/css2?family=Open+Sans:wght@300;400;700;800&display=swap" rel="stylesheet">
<style>
  :root {
    --page-bg: #2b2b2d;
    --river-teal: #4bb8c8;
    --grass-green: #8cc63f;
    --grass-dark: #6aa82e;
    --sun-yellow: #f6d12a;
    --ink: #3d3d3f;
    --ink-soft: #5a5a5c;
    --sky-top: #bcd6ec;
    --sky-bottom: #f4f8fb;
    --white: #ffffff;
  }
  * { box-sizing: border-box; margin: 0; padding: 0; }
  html, body { width: 1200px; height: 793px; overflow: hidden; }
  body {
    background: var(--page-bg);
    font-family: "Open Sans", Arial, sans-serif;
    color: var(--ink);
    position: relative;
  }
  .brochure {
    position: absolute;
    left: 50px; top: 36px;
    width: 1100px; height: 721px;
    background: var(--white);
    overflow: hidden;
  }
  .brand-bar { height: 14px; background: var(--river-teal); }
  .hero {
    position: relative;
    height: 280px;
    background: linear-gradient(180deg, var(--sky-top) 0%, #dbe9f4 45%, var(--sky-bottom) 100%);
  }
  .hero-photo {
    position: absolute;
    right: 0; top: 0;
    width: 430px; height: 280px;
    background: linear-gradient(90deg, rgba(210,226,238,0) 0%, #8a8c6a 35%, #54603a 60%, #3a4128 85%, #c9dae8 100%);
  }
  .intro {
    position: absolute;
    left: 38px; top: 66px;
    width: 320px;
    font-weight: 300;
    font-size: 12.5px;
    line-height: 1.55;
    color: var(--ink-soft);
  }
  .intro strong, .sunshine strong { font-weight: 800; color: var(--ink); }
  .intro .lead { font-size: 18px; }
  .intro strong.mid, .sunshine strong { font-size: 14.5px; }
  .sunshine {
    position: absolute;
    left: 382px; top: 70px;
    width: 260px;
    font-weight: 300;
    font-size: 13px;
    line-height: 1.55;
    color: var(--ink-soft);
  }
  .club-mark {
    position: absolute;
    left: 104px; top: 244px;
    display: flex; align-items: center; gap: 8px;
    font-size: 12px; font-weight: 400;
    letter-spacing: 2px; text-transform: uppercase;
    color: var(--ink-soft);
  }
  .club-mark .dot {
    width: 24px; height: 24px; border-radius: 50%;
    background: var(--river-teal);
  }
  .divider { height: 6px; background: var(--grass-green); }
  .features {
    position: relative;
    height: 330px;
    background: linear-gradient(180deg, #fbfcfd 0%, #eef4f8 40%, #e6eef2 48%);
  }
  .feature {
    position: absolute; top: 20px;
    font-size: 8.6px; font-weight: 300; line-height: 1.45;
    color: var(--ink-soft);
  }
  .feature strong { font-weight: 800; color: var(--ink); }
  .feature-courses { left: 44px; width: 290px; }
  .feature-courses strong { font-size: 14px; }
  .feature-packages { left: 382px; width: 300px; }
  .feature-packages strong, .feature-clubhouse strong { font-size: 12px; }
  .feature-clubhouse { left: 722px; width: 300px; }
  .course-photo {
    position: absolute;
    left: 0; bottom: 0;
    width: 100%; height: 250px;
    background:
      linear-gradient(180deg, rgba(230,238,242,0) 0%, rgba(58,74,40,0.85) 30%, #3c4a26 50%, #7d9440 62%, #98ad4c 80%, #6f8a30 100%);
  }
  .sun-stripe { height: 6px; background: var(--sun-yellow); }
  .footer-bar {
    height: 41px;
    background: linear-gradient(90deg, var(--grass-green), var(--grass-dark) 50%, var(--grass-green));
    display: flex; align-items: center; justify-content: center;
    color: var(--white); font-size: 13px; font-weight: 400;
  }
  .folds { position: absolute; inset: 0; pointer-events: none; }
</style>
</head>
<body>
  <main class="brochure">
    <div class="brand-bar"></div>

    <section class="hero">
      <div class="hero-photo" role="img" aria-label="Golfer mid-swing with a driver against a clear sky"></div>

      <p class="intro">
        <strong class="lead">THE SECRET IS OUT!</strong> Along the Mighty Kellaway, Brindlemere Golf Course is maintained at the highest levels of excellence unsurpassed on the River. This magnificent <strong class="mid">36 HOLE CHAMPIONSHIP SAND-BELT</strong> course offers a challenge to golfers of all levels and hosts the annual Southern Pro Trainee Championships.
      </p>

      <p class="sunshine">
        With in excess of <strong>300 DAYS OF SUNSHINE EACH YEAR,</strong> the region boasts more sunny weather than the Gold Coast with two superb golf courses (President's and Captain's) that are suitable to play all year round.
      </p>

      <div class="club-mark"><span class="dot"></span>Brindlemere Golf Club</div>
    </section>

    <div class="divider"></div>

    <section class="features">
      <div class="course-photo" role="img" aria-label="Golf course green with a sand bunker and gum trees at sunset"></div>

      <p class="feature feature-courses">
        <strong>THE COURSES</strong> abound with our native flora and fauna and water features are home to an amazing abundance of birdlife. Kangaroos regularly frequent the lush fairways to graze and laze in the shade during the warmth of the afternoon sun.
      </p>
      <p class="feature feature-packages">
        <strong>OUTSTANDING VALUE GOLF PACKAGES</strong> offer a range of accommodation options within easy walking distance of the Clubhouse. Let our friendly staff make your stay an unforgettable golfing experience.
      </p>
      <p class="feature feature-clubhouse">
        <strong>OUR MODERN CLUBHOUSE</strong> boasts full NSW club facilities and invites members and visitors to choose seating areas overlooking the course or dine Al Fresco on the balcony amongst the nature. Our Bistro is open all day every day for full bistro meals as well as light snacks.
      </p>
    </section>

    <div class="sun-stripe"></div>
    <footer class="footer-bar">www.brindlemeregolf.com.au</footer>

    <svg class="folds" width="1100" height="721" aria-hidden="true">
      <line x1="356" y1="0" x2="356" y2="721" stroke="#000" stroke-opacity="0.05" stroke-width="6"/>
      <line x1="704" y1="0" x2="704" y2="721" stroke="#000" stroke-opacity="0.05" stroke-width="6"/>
    </svg>
  </main>
</body>
</html>
```